Martin K Doyle DDS (dentist) needs a business card/business logo design

I would like an eye-catchingly conservative or elegant graphic presentation of my business name with the elements: prevention, restoration, and cosmetics (these are the services I'd like to emphasize) .
The business card would have room for address lines, phone and fax, web address. No standard teeth or oral representations please. Should communicate professionalism. Whatever color scheme works.

Thank you

Target Market(s)

I just want a good looking business card

Industry/Entity Type

Conservative

Contact Information for Business Card

Adress: 4173 Brisford Ave Lakewood CA 90716 Phone: 562 430 5926 FAX 562 430 6384 Web: Pinegrovedental.com

Font styles to use
Sans Serif

Colors
0255a3

Requirements
Must have
• business name with the elements: prevention, restoration, and cosmetics (these are the services I'd like to emphasize)
• communicates professionalism
Nice to have
• eye catching but not flashy graphics
Should not have
• no pictures of teeth or dental instruments

```html
<!DOCTYPE html>
<html lang="en">
<head>
<meta charset="utf-8">
<title>Martin Doyle DDS – Business Card</title>
<link href="https://fonts.googleapis.com/css2?family=Arimo:wght@400;700&display=swap" rel="stylesheet">
<style>
  :root {
    --page-bg: #ece9e4;
    --card-white: #f4f4f2;
    --card-blue: #5ea6dc;
    --ink-dark: #2b2b2b;
    --accent-red: #b1201f;
    --text-light: #ffffff;
    --service-text: #e6f1fa;
  }
  html, body {
    margin: 0;
    padding: 0;
    width: 1200px;
    height: 1075px;
    overflow: hidden;
    background: var(--page-bg);
    font-family: "Arimo", Arial, sans-serif;
  }
  .business-card {
    position: absolute;
    left: 100px;
    top: 252px;
    width: 1000px;
    height: 571px;
    background: var(--card-blue);
    box-shadow: 0 12px 30px rgba(0,0,0,0.18);
    overflow: hidden;
  }
  .card-header {
    position: absolute;
    left: 0; top: 0;
    width: 100%;
    height: 258px;
    background: var(--card-white);
  }
  .brand {
    position: absolute;
    left: 228px;
    top: 62px;
  }
  .brand-name {
    margin: 0;
    font-weight: 700;
    font-size: 64px;
    line-height: 1;
    color: var(--ink-dark);
    letter-spacing: -0.5px;
    white-space: nowrap;
  }
  .brand-name .credential { color: var(--accent-red); }
  .brand-rule {
    height: 4px;
    background: var(--accent-red);
    margin-top: 8px;
  }
  .brand-practice {
    margin: 6px 0 0;
    text-align: right;
    font-weight: 700;
    font-size: 22px;
    color: var(--ink-dark);
  }
  .services {
    position: absolute;
    top: 284px;
    left: 0;
    width: 100%;
    margin: 0;
    padding: 0;
    list-style: none;
  }
  .service {
    position: absolute;
    display: flex;
    align-items: center;
    gap: 10px;
    font-weight: 700;
    font-size: 25px;
    letter-spacing: 0.5px;
    color: var(--service-text);
  }
  .service svg { width: 24px; height: 24px; }
  .service--prevention { left: 118px; }
  .service--restoration { left: 412px; }
  .service--cosmetics { left: 712px; }
  .contact {
    position: absolute;
    top: 384px;
    left: 130px;
    width: 820px;
    text-align: center;
    color: var(--text-light);
    font-size: 22px;
    line-height: 38px;
    letter-spacing: 1.5px;
  }
  .contact p { margin: 0; white-space: nowrap; }
</style>
</head>
<body>
  <section class="business-card">
    <header class="card-header">
      <div class="brand">
        <h1 class="brand-name">Martin Doyle <span class="credential">DDS</span></h1>
        <div class="brand-rule"></div>
        <p class="brand-practice">Pinegrove Dentistry</p>
      </div>
    </header>

    <ul class="services">
      <li class="service service--prevention">
        <svg viewBox="0 0 24 24" aria-hidden="true"><circle cx="12" cy="12" r="10.5" fill="none" stroke="#fff" stroke-width="2"/><path d="M8 7 L17 12 L8 17 L10.5 12 Z" fill="#fff"/></svg>
        Prevention
      </li>
      <li class="service service--restoration">
        <svg viewBox="0 0 24 24" aria-hidden="true"><circle cx="12" cy="12" r="10.5" fill="none" stroke="#fff" stroke-width="2"/><path d="M8 7 L17 12 L8 17 L10.5 12 Z" fill="#fff"/></svg>
        Restoration
      </li>
      <li class="service service--cosmetics">
        <svg viewBox="0 0 24 24" aria-hidden="true"><circle cx="12" cy="12" r="10.5" fill="none" stroke="#fff" stroke-width="2"/><path d="M8 7 L17 12 L8 17 L10.5 12 Z" fill="#fff"/></svg>
        Cosmetics
      </li>
    </ul>

    <address class="contact">
      <p>Address: 4173 Brisford Ave Lakewood CA 90716</p>
      <p>Phone: 562 430 5926, Fax: 562 430 6384</p>
      <p>Web: www.pinegrovedental.com, Email: frontdesk@pinegrovedental.com</p>
    </address>
  </section>
</body>
</html>
```